Business Card for Restaurant Vendal

This project consist of creating 2 design for business card of restaurant named Vendal.

The attached specs below are 'ONLY SUGGESTION' if you have others ideas. You are welcome to post it.

1) Restaurant Card

Adresse:
2784 Côte du Pinard Vert
Montréal (Qc) H4K 3T8

Website:
www.ven-dal.ca

Phone:
438-719-2046

2) Employee Card

Name: Lorna Pik
Title: Owner

Address:
2784 Côte du Pinard Vert
Montréal (Qc) H4K 3T8

Email:lorna@ven-dal.ca
Phone Number:438-719-2046
Cellphone Number:514-830-4162

 The attached specs are 'ONLY SUGGESTION' if you have others ideas.  You are welcome to post it.

Industry/Entity Type

Restaurant

Requirements
Must have
• UV Card Spot

To print Spot UV business cards you would have to submit 2 files for each side. The first file "base" would be your regular design file as it would have been in any other case. The 2nd file "UV mask" is a black/white file. The BLACK color will indicate the areas that will be covered with the UV high gloss finish. To upload the files, please combine front design and front mask file in one P
Nice to have
• 1) The font of the logo should be ink effect
2) black background with wallpaper effect
3) The specs below are 'ONLY SUGGESTION' if you have others ideas. You are welcome to post it.

```html
<!DOCTYPE html>
<html lang="fr">
<head>
<meta charset="utf-8">
<title>Restaurant Vendal – Business Cards</title>
<link rel="stylesheet" href="https://fonts.googleapis.com/css2?family=Arimo:wght@400;700&family=Noto+Sans+JP:wght@400&display=swap">
<style>
  :root {
    --stage: #d9d6d1;
    --card-black: #221f20;
    --card-black-light: #2d2a2b;
    --ink-white: #ffffff;
    --text-soft: #e9e6e4;
    --accent-red: #e3231b;
    --accent-red-deep: #b8160f;
    --art-dark: #171516;
    --art-mid: #2b2829;
  }
  * { box-sizing: border-box; margin: 0; padding: 0; }
  html, body {
    width: 1200px; height: 900px; overflow: hidden;
    background: var(--stage);
    font-family: "Arimo", Arial, sans-serif;
  }
  .stage { position: relative; width: 1200px; height: 900px; }

  .card {
    position: absolute;
    width: 540px; height: 300px;
    background:
      repeating-linear-gradient(90deg, rgba(255,255,255,0.025) 0 1px, transparent 1px 3px),
      linear-gradient(135deg, var(--card-black-light), var(--card-black));
    box-shadow: 0 14px 30px rgba(0,0,0,0.35);
    overflow: hidden;
    color: var(--text-soft);
  }

  /* Front card */
  .card--front { left: 220px; top: 140px; }
  .front__art {
    position: absolute; left: 0; top: 20px;
    width: 190px; height: 260px;
    background: linear-gradient(180deg, var(--art-mid), var(--art-dark));
  }
  .brand {
    position: absolute; left: 240px; top: 70px;
    display: flex; align-items: flex-start; gap: 6px;
  }
  .brand__name {
    font-weight: 700; font-size: 64px; line-height: 1;
    color: var(--ink-white);
  }
  .brand__dot {
    width: 12px; height: 12px; border-radius: 50%;
    background: var(--accent-red); margin-top: 2px;
  }
  .front__tagline {
    position: absolute; left: 250px; top: 160px;
    font-size: 17px; color: var(--ink-white);
  }
  .front__tagline .sep { color: var(--accent-red); margin: 0 4px; }

  /* Back card */
  .card--back { left: 440px; top: 470px; }
  .back__kana {
    position: absolute; left: 26px; top: 22px;
    font-family: "Noto Sans JP", sans-serif; font-size: 20px; color: var(--ink-white);
  }
  .person { position: absolute; left: 26px; top: 72px; }
  .person__name { font-size: 20px; color: var(--ink-white); }
  .person__title { font-size: 12px; margin-top: 1px; }
  .contact {
    position: absolute; left: 26px; top: 124px;
    font-size: 12.5px; line-height: 1.35;
    border-collapse: collapse;
  }
  .contact td { padding: 0; }
  .contact td:first-child { padding-right: 8px; }
  .address {
    position: absolute; left: 26px; top: 198px;
    font-size: 12.5px; line-height: 1.4; text-transform: uppercase;
  }
  .back__art {
    position: absolute; left: 320px; top: 50px;
    width: 200px; height: 230px;
    background: linear-gradient(180deg, var(--accent-red), var(--accent-red-deep));
  }
</style>
</head>
<body>
<main class="stage">

  <section class="card card--front" aria-label="Restaurant card, front">
    <div class="front__art" role="img" aria-label="Dark paper lantern illustration with glossy spot UV finish"></div>
    <div class="brand">
      <span class="brand__name">Vendal</span>
      <span class="brand__dot"></span>
    </div>
    <p class="front__tagline">Resto-Bar Japonais<span class="sep">•</span>Izakaya</p>
  </section>

  <section class="card card--back" aria-label="Employee card">
    <p class="back__kana" lang="ja">ヴェンダル</p>
    <div class="person">
      <p class="person__name">Lorna Pik</p>
      <p class="person__title">Owner</p>
    </div>
    <table class="contact">
      <tr><td>Phone:</td><td>438-719-2046</td></tr>
      <tr><td>Mobile:</td><td>514-830-4162</td></tr>
      <tr><td>Email:</td><td>lorna@ven-dal.ca</td></tr>
    </table>
    <p class="address">2784 Côte du Pinard Vert<br>Montréal (Qc) H4K 3T8</p>
    <div class="back__art" role="img" aria-label="Red izakaya paper lantern illustration with brush characters"></div>
  </section>

</main>
</body>
</html>
```